Business Card Design Project

The business card is for an educational company that provides personalised tuition to students.

The company logo is in orange and blue (as provided) and should be included in the name card design

The philosophy of the company is to make learning a comfortable experience for student as such design of the namecard should look fresh and has a bit of the 'wow' factor. Some of the namecard design that appeals to me are as uploaded under Sample Design.

The particulars that need to be provided are:
(1): Company Name (Quillmont Education)
(1): Name
(2): Educational qualifications which will appear below name
(3): Mobile number
(4): Email address
(5): Website

Industry/Entity Type

Business

Requirements
Must have
• (1): Company Logo

(2): The card background should preferably be coloured both for the front side and back.

(3): The choice of font is important as part of the selection consideration. There is no preferred font that I have selected, designer is free to choose the font that will complement their design.

```html
<!DOCTYPE html>
<html lang="en">
<head>
<meta charset="utf-8">
<title>Quillmont Education – Business Card</title>
<link rel="stylesheet" href="https://fonts.googleapis.com/css2?family=Quicksand:wght@400;500;700&display=swap">
<style>
  :root {
    --page-bg: #e6e9ec;
    --card-bg: #a6d3ef;
    --band-blue: #3d84c6;
    --band-orange: #eb8b34;
    --mark-orange: #ee7a22;
    --ink-grey: #565758;
    --ink-white: #ffffff;
  }
  * { box-sizing: border-box; margin: 0; padding: 0; }
  html, body {
    width: 1200px; height: 960px; overflow: hidden;
    background: var(--page-bg);
    font-family: "Quicksand", "Trebuchet MS", sans-serif;
  }
  .sheet { position: relative; width: 1200px; height: 960px; }
  .card {
    position: absolute; left: 250px;
    width: 700px; height: 400px;
    background: var(--card-bg);
    box-shadow: 0 6px 18px rgba(0,0,0,.18);
    overflow: hidden;
  }
  .card--front { top: 60px; }
  .card--back { top: 500px; }

  .brand { position: absolute; display: flex; align-items: center; gap: 22px; }
  .brand__square { background: var(--mark-orange); border-radius: 14px; flex: none; }
  .brand__name {
    color: var(--ink-grey); font-weight: 700; line-height: 1.02;
  }
  .card--front .brand { left: 40px; top: 36px; }
  .card--front .brand__square { width: 118px; height: 118px; }
  .card--front .brand__name { font-size: 50px; }
  .card--back .brand { left: 50%; top: 62px; transform: translateX(-50%); }
  .card--back .brand__square { width: 104px; height: 104px; }
  .card--back .brand__name { font-size: 44px; }

  .band { position: absolute; display: flex; align-items: center; color: var(--ink-white); }
  .band--identity {
    left: 0; top: 212px; width: 585px; height: 50px;
    background: var(--band-blue); padding-left: 26px;
  }
  .person-name { font-size: 31px; font-weight: 500; }
  .person-role { font-size: 19px; font-weight: 500; margin-left: 8px; padding-left: 8px; border-left: 2px solid var(--ink-white); line-height: 1; }
  .band--contact {
    left: 190px; top: 272px; width: 510px; height: 52px;
    background: var(--band-orange); padding-left: 70px; gap: 34px;
  }
  .band--web {
    left: 20px; top: 248px; width: 620px; height: 50px;
    background: var(--band-orange); justify-content: center;
  }
  .contact-item { display: flex; align-items: center; gap: 10px; font-size: 17px; font-weight: 500; }
  .icon { width: 16px; height: 16px; flex: none; }
</style>
</head>
<body>
<main class="sheet">

  <section class="card card--front" aria-label="Card front">
    <div class="brand">
      <span class="brand__square"></span>
      <p class="brand__name">Quillmont<br>Education</p>
    </div>
    <div class="band band--identity">
      <span class="person-name">Avery Lindqvist</span>
      <span class="person-role">Operation Manager</span>
    </div>
    <div class="band band--contact">
      <span class="contact-item">
        <svg class="icon" viewBox="0 0 16 16" aria-hidden="true"><rect x="4" y="1" width="8" height="14" rx="1.5" fill="none" stroke="#fff" stroke-width="1.5"/><rect x="6" y="3.5" width="4" height="5" fill="#fff"/></svg>
        (555) 48 210 36 19
      </span>
      <span class="contact-item">
        <svg class="icon" viewBox="0 0 16 16" aria-hidden="true"><rect x="1.5" y="3.5" width="13" height="9" fill="none" stroke="#fff" stroke-width="1.5"/><path d="M1.5 3.5 8 9l6.5-5.5" fill="none" stroke="#fff" stroke-width="1.5"/></svg>
        name@quillmont-edu.com
      </span>
    </div>
  </section>

  <section class="card card--back" aria-label="Card back">
    <div class="brand">
      <span class="brand__square"></span>
      <p class="brand__name">Quillmont<br>Education</p>
    </div>
    <div class="band band--web">
      <span class="contact-item">
        <svg class="icon" viewBox="0 0 16 16" aria-hidden="true"><circle cx="8" cy="8" r="6.5" fill="none" stroke="#fff" stroke-width="1.5"/><ellipse cx="8" cy="8" rx="2.8" ry="6.5" fill="none" stroke="#fff" stroke-width="1.2"/><path d="M1.5 8h13" stroke="#fff" stroke-width="1.2"/></svg>
        www.quillmont-education.com
      </span>
    </div>
  </section>

</main>
</body>
</html>
```